Ferris Contracting LLC Business Card Design

I am looking for a creative and unique business card design. We are a commercial construction general contractor. With the name "FERRIS" Contracting, I am hoping to see some neat designs that correlate with the name.

```html
<!DOCTYPE html>
<html lang="en">
<head>
<meta charset="utf-8">
<title>Ferris Contracting LLC – Business Card</title>
<link rel="stylesheet" href="https://fonts.googleapis.com/css2?family=Montserrat:wght@400;500;700;800&display=swap">
<style>
  :root {
    --bg-light: #d4d4d4;
    --bg-dark: #a9a9a9;
    --card: #222223;
    --card-deep: #1b1b1c;
    --blue: #1e8ad6;
    --blue-bright: #2fa3ee;
    --silver: #d9d9d9;
    --silver-dark: #8c8c8c;
    --text: #f2f2f2;
    --emboss: #2f2f30;
  }
  * { margin: 0; padding: 0; box-sizing: border-box; }
  html, body { width: 1200px; height: 802px; overflow: hidden; }
  body {
    background: radial-gradient(ellipse at 40% 20%, var(--bg-light), var(--bg-dark));
    font-family: "Montserrat", sans-serif;
    position: relative;
  }
  .card {
    position: absolute;
    width: 540px;
    height: 309px;
    border-radius: 18px;
    background: var(--card);
    overflow: hidden;
    box-shadow: 0 14px 30px rgba(0,0,0,.35);
  }
  .card--front { left: 40px; top: 246px; }
  .card--back { left: 620px; top: 246px; background: var(--card-deep); }

  .card__band { position: absolute; inset: 0; }

  .brand {
    position: absolute;
    left: 34px;
    top: 40px;
    display: flex;
    align-items: center;
    gap: 10px;
  }
  .brand__dot {
    width: 14px; height: 14px; border-radius: 50%;
    background: var(--blue);
  }
  .brand__name {
    font-weight: 800;
    font-size: 38px;
    letter-spacing: 1px;
    color: var(--blue);
  }

  .person {
    position: absolute;
    right: 150px;
    top: 30px;
    text-align: right;
  }
  .person__name {
    font-weight: 700;
    font-size: 19px;
    color: var(--blue-bright);
    letter-spacing: .5px;
  }
  .person__role {
    font-size: 13px;
    color: var(--text);
    margin-top: 2px;
  }

  .contact {
    position: absolute;
    left: 34px;
    top: 150px;
    color: var(--text);
    font-size: 13px;
    line-height: 1.45;
  }
  .contact__address { margin-bottom: 8px; }
  .contact__list { list-style: none; }
  .contact__item { display: flex; align-items: center; gap: 8px; }
  .contact__icon { width: 11px; height: 11px; flex: none; }

  .back-mark {
    position: absolute;
    inset: 0;
    display: flex;
    align-items: center;
    justify-content: center;
    font-weight: 800;
    font-size: 68px;
    letter-spacing: 3px;
    color: var(--emboss);
  }
</style>
</head>
<body>

<section class="card card--front" aria-label="Business card front">
  <svg class="card__band" viewBox="0 0 540 309" aria-hidden="true">
    <defs>
      <linearGradient id="silver" x1="0" y1="0" x2="1" y2="1">
        <stop offset="0" stop-color="#f1f1f1"/>
        <stop offset=".5" stop-color="#9a9a9a"/>
        <stop offset="1" stop-color="#e2e2e2"/>
      </linearGradient>
      <linearGradient id="shade" x1="0" y1="0" x2="1" y2="0">
        <stop offset="0" stop-color="#2a2a2b"/>
        <stop offset="1" stop-color="#3a3a3b"/>
      </linearGradient>
    </defs>
    <polygon points="540,0 540,309 430,309" fill="url(#shade)"/>
    <polygon points="540,60 540,80 440,309 420,309" fill="url(#silver)"/>
    <rect x="480" y="0" width="60" height="14" fill="var(--blue)"/>
    <rect x="300" y="299" width="126" height="10" fill="var(--blue)"/>
  </svg>

  <div class="brand">
    <span class="brand__dot"></span>
    <span class="brand__name">FERRIS</span>
  </div>

  <div class="person">
    <div class="person__name">DANA MERCER</div>
    <div class="person__role">CEO/Founder</div>
  </div>

  <div class="contact">
    <p class="contact__address">417 Kestrel Avenue, Suite 210<br>Northfield, AB 55412</p>
    <ul class="contact__list">
      <li class="contact__item">
        <svg class="contact__icon" viewBox="0 0 12 12"><path d="M2 1l2.5 0 1 3-1.5 1a6 6 0 0 0 3 3l1-1.5 3 1V10a1 1 0 0 1-1 1A9 9 0 0 1 1 2a1 1 0 0 1 1-1z" fill="var(--blue)"/></svg>
        (555)-014-2286
      </li>
      <li class="contact__item">
        <svg class="contact__icon" viewBox="0 0 12 12"><rect x="1" y="2.5" width="10" height="7" rx="1" fill="var(--blue)"/><path d="M1.5 3l4.5 3.5L10.5 3" stroke="var(--card)" fill="none"/></svg>
        info@ferriscontracting.com
      </li>
      <li class="contact__item">
        <svg class="contact__icon" viewBox="0 0 12 12"><circle cx="6" cy="6" r="5" fill="var(--blue)"/><path d="M1 6h10M6 1c2 2 2 8 0 10M6 1c-2 2-2 8 0 10" stroke="var(--card)" stroke-width=".8" fill="none"/></svg>
        www.ferriscontracting.com
      </li>
    </ul>
  </div>
</section>

<section class="card card--back" aria-label="Business card back">
  <div class="back-mark">FERRIS</div>
</section>

</body>
</html>
```